ORVANE SYSTEMS LTD

See website just wanted it updated and more fresh ; https://www.orvane-sys.co.uk

Coding

Coded - Design and coding required

Colors

Designer to choose colors to be used in the design.

```html
<!DOCTYPE html>
<html lang="en">
<head>
<meta charset="utf-8">
<title>Orvane Systems – Education, Support &amp; Installation</title>
<link rel="stylesheet" href="https://fonts.googleapis.com/css2?family=Comfortaa:wght@500;700&family=Poppins:wght@300;400;500&display=swap">
<style>
:root{
  --blue:#0b6ec0;
  --blue-dark:#085da3;
  --orange:#f26522;
  --pale:#eef6fd;
  --ink:#555d66;
  --navy:#0f1a28;
  --white:#fff;
}
*{box-sizing:border-box;margin:0;padding:0}
html,body{width:1200px;height:3417px;overflow:hidden}
body{position:relative;font-family:"Poppins",sans-serif;color:var(--ink);background:var(--white)}
.abs{position:absolute}
.heading{font-family:"Comfortaa",sans-serif;font-weight:700;color:var(--blue)}
.accent{border-bottom:3px solid var(--orange);padding-bottom:2px}
.btn{position:absolute;display:flex;align-items:center;justify-content:center;background:var(--orange);color:var(--white);font-family:"Poppins",sans-serif;font-weight:500;font-size:19px;letter-spacing:.3px;border-radius:4px}

/* top bar */
.topbar{left:0;top:0;width:1200px;height:41px;background:var(--blue);color:var(--white);font-size:16px}
.topbar .phone{left:76px;top:9px;display:flex;align-items:center;gap:10px}
.topbar .phone i{width:28px;height:28px;border-radius:50%;background:var(--orange);display:flex;align-items:center;justify-content:center}
.topbar .account{right:77px;top:10px;font-size:15px}

/* nav */
.nav{left:0;top:41px;width:1200px;height:73px;background:var(--white)}
.nav a{position:absolute;top:30px;font-size:14px;color:#222;text-decoration:none;letter-spacing:.2px}
.nav a.active{color:var(--orange)}
.nav a.active::before{content:"";position:absolute;left:-14px;top:6px;width:6px;height:6px;background:var(--orange)}
.brand-box{left:467px;top:26px;width:266px;height:104px;background:var(--white);border-radius:8px;box-shadow:0 2px 10px rgba(0,0,0,.12);display:flex;flex-direction:column;align-items:center;justify-content:center;z-index:3}
.brand-box .name{font-family:"Comfortaa",sans-serif;font-weight:700;font-size:34px;color:var(--blue)}
.brand-box .tag{font-size:11px;color:var(--blue);margin-top:2px}

/* hero */
.hero{left:0;top:114px;width:1200px;height:562px;border-radius:0 80px 0 80px;background:linear-gradient(120deg,#6b4e3a 0%,#3d4c5c 45%,#243041 70%,#7b6a5a 100%);overflow:hidden}
.hero h1{position:absolute;left:0;top:208px;width:1200px;text-align:center;font-family:"Comfortaa",sans-serif;font-weight:700;font-size:41px;line-height:49px;color:var(--white)}
.hero .arrow{position:absolute;top:258px;width:46px;height:46px;border-radius:50%;border:1px solid rgba(255,255,255,.6)}

/* about */
.about{left:0;top:676px;width:1200px;height:504px;background:var(--pale)}
.about h2{position:absolute;left:164px;top:88px;font-size:40px;white-space:nowrap}
.about .sub{position:absolute;left:164px;top:144px;font-size:15px;color:var(--blue)}
.about .copy-block{position:absolute;left:162px;top:176px;width:420px}
.about .copy-block p{font-size:15px;line-height:27px;color:var(--ink);margin-bottom:9px}
.about .copy-block .btn{position:static;display:inline-flex;width:167px;height:51px;margin-top:15px}
.about .photo{position:absolute;left:692px;top:68px;width:342px;height:371px;border-radius:0 22px 0 22px;background:linear-gradient(135deg,#55687a,#1f2a36);box-shadow:8px 8px 0 var(--blue)}

/* services */
.section-title{left:0;width:1200px;text-align:center;font-size:42px;line-height:48px}
.service{width:300px;text-align:center}
.service h3{font-family:"Comfortaa",sans-serif;font-weight:700;font-size:24px;color:var(--blue)}
.service p{margin-top:14px;font-size:15px;line-height:27px;color:var(--ink)}
.service .more{display:inline-block;margin-top:20px;font-size:15px;color:var(--orange);text-decoration:underline}
.service .more::after{content:"";display:inline-block;margin-left:8px;border-left:7px solid var(--orange);border-top:5px solid transparent;border-bottom:5px solid transparent}
.support{left:0;top:1628px;width:1200px;height:650px;background:var(--blue);border-radius:66px 0 66px 0}
.thumb{width:176px;height:176px;border-radius:50%;border:8px solid var(--white);box-shadow:0 2px 8px rgba(0,0,0,.2);z-index:2}
.support h2{position:absolute;left:0;top:128px;width:1200px;text-align:center;color:var(--white);font-size:44px;line-height:48px;font-weight:500}
.support p{position:absolute;left:0;top:250px;width:1200px;text-align:center;color:var(--white);font-size:15px;line-height:27px}
.support .photo{position:absolute;left:256px;top:333px;width:688px;height:171px;background:linear-gradient(90deg,#d9d6d0,#6e6861 50%,#3a2e28)}

/* testimonial */
.kid{left:159px;top:2466px;width:398px;height:483px;background:linear-gradient(180deg,#d9e6f3,#7ea7d4);border-radius:40% 40% 6px 6px}
.quote-mark{left:660px;top:2549px;width:74px;height:74px;border-radius:50%;background:var(--orange);display:flex;align-items:center;justify-content:center;font-family:"Comfortaa",sans-serif;font-weight:700;color:var(--white);font-size:54px;line-height:1;padding-top:22px}
.quote{left:658px;top:2646px;width:446px;font-size:15px;line-height:27px;color:var(--ink)}
.author{left:683px;top:2807px;width:400px;font-family:"Comfortaa",sans-serif;font-weight:700;font-size:18px;line-height:29px;color:var(--blue)}
.author::before{content:"";position:absolute;left:-25px;top:13px;width:14px;height:3px;background:var(--blue)}

/* cta band */
.cta{left:0;top:2949px;width:1200px;height:93px;background:var(--blue)}
.cta .line{position:absolute;left:175px;top:33px;font-family:"Comfortaa",sans-serif;font-weight:700;font-size:23px;color:var(--white)}

/* footer */
.footer{left:0;top:3042px;width:1200px;height:375px;background:var(--navy);color:#c9d0d8}
.footer .brand{position:absolute;left:115px;top:108px;width:240px;text-align:center}
.footer .brand .name{font-family:"Comfortaa",sans-serif;font-weight:700;font-size:36px;color:var(--white)}
.footer .brand .tag{font-size:11px;color:var(--white)}
.social{position:absolute;top:189px;width:48px;height:48px;border-radius:50%}
.footer h4{position:absolute;top:30px;font-family:"Poppins",sans-serif;font-weight:500;font-size:18px;letter-spacing:.5px;color:var(--blue)}
.footer h4 .accent{padding-bottom:6px}
.footer .news{position:absolute;left:422px;top:90px;width:320px;font-size:15px;line-height:28px;color:#c9d0d8}
.footer .field{position:absolute;left:422px;top:155px;width:311px;height:52px;background:#1c2736;color:#d7dde4;font-size:14px;padding:18px 14px}
.contact-item{position:absolute;left:839px;font-size:15px;color:#c9d0d8}
.contact-icon{position:absolute;left:795px}
.footer .rule{position:absolute;left:76px;top:310px;width:1048px;height:1px;background:#2a3646}
.footer .copy{position:absolute;left:0;top:330px;width:1200px;text-align:center;font-size:13px;color:#9aa5b1}
.footer .copy span{color:var(--blue)}
</style>
</head>
<body>

<header>
  <div class="abs topbar">
    <div class="abs phone"><i><svg width="14" height="14" viewBox="0 0 24 24"><path fill="#fff" d="M6.6 10.8a15 15 0 0 0 6.6 6.6l2.2-2.2a1 1 0 0 1 1-.25 11.4 11.4 0 0 0 3.6.57 1 1 0 0 1 1 1V20a1 1 0 0 1-1 1A17 17 0 0 1 3 4a1 1 0 0 1 1-1h3.5a1 1 0 0 1 1 1 11.4 11.4 0 0 0 .57 3.6 1 1 0 0 1-.25 1z"/></svg></i>0161 555 0142</div>
    <div class="abs account">
      <svg width="14" height="16" viewBox="0 0 14 16" style="vertical-align:-2px"><circle cx="7" cy="4" r="3.5" fill="#f26522"/><path d="M0 16a7 7 0 0 1 14 0z" fill="#f26522"/></svg>
      Signup &nbsp;/ Login
    </div>
  </div>
  <nav class="abs nav">
    <a class="active" style="left:197px">HOME</a>
    <a style="left:271px">SERVICES</a>
    <a style="left:362px">ABOUT US</a>
    <a style="left:767px">HELPDESK</a>
    <a style="left:860px">CONTACT</a>
    <svg class="abs" style="left:960px;top:31px" width="16" height="16" viewBox="0 0 16 16"><circle cx="6.5" cy="6.5" r="5" fill="none" stroke="#222" stroke-width="2"/><path d="M10 10l5 5" stroke="#222" stroke-width="2.4"/></svg>
  </nav>
  <div class="abs brand-box">
    <div class="name">Orvane</div>
    <div class="tag">Education Support and Installation</div>
  </div>
</header>

<section class="abs hero" role="img" aria-label="Teacher helping primary school pupils working on laptops in a classroom">
  <span class="arrow" style="left:14px"></span>
  <span class="arrow" style="right:14px"></span>
  <h1>Education, Support &amp; Installation<br>of All Technologies</h1>
  <span class="btn" style="left:516px;top:333px;width:167px;height:53px">CONTACT US</span>
</section>

<section class="abs about">
  <h2 class="heading">About Orvane <span class="accent">Systems</span></h2>
  <div class="sub">Education Support &amp; Installation</div>
  <div class="copy-block">
    <p>Orvane Systems is a registered UK Limited Company. Our goal is to provide full ICT support with excellent service to the education sector.</p>
    <p>Extra support visits during ofsted inspections. Remote access support for servers, computers and laptops. Email &amp; Telephone Support</p>
    <span class="btn">LEARN MORE</span>
  </div>
  <div class="photo" role="img" aria-label="Technician working on a laptop in a server room"></div>
</section>

<h2 class="abs heading section-title" style="top:1236px">What We <span class="accent">Do</span></h2>

<div class="abs service" style="left:120px;top:1340px">
  <h3>ICT Support</h3>
  <p>We provide a wide range of ICT support packages, which all include regular onsite</p>
  <span class="more">Read More</span>
</div>
<div class="abs service" style="left:450px;top:1340px">
  <h3>Hardware Sales</h3>
  <p>We supply and install hardware from the world's leading manufacturers including all brands</p>
  <span class="more">Read More</span>
</div>
<div class="abs service" style="left:785px;top:1340px">
  <h3>Cloud &amp; Hosting</h3>
  <p>We offer an extensive range of cloud &amp; hosting services including websites, domains,</p>
  <span class="more">Read More</span>
</div>

<section class="abs support">
  <h2 class="heading">Complete Primary &amp;<br>Secondary School <span class="accent">Support</span></h2>
  <p>We offer support in all aspects of ICT in education, from technical faults to assisting teachers and<br>coordinators to meet the requirements of the computing curriculum</p>
  <div class="photo" role="img" aria-label="Person writing code on a laptop"></div>
  <span class="btn" style="left:496px;top:528px;width:208px;height:51px">FIND OUT MORE</span>
</section>

<div class="abs thumb" style="left:180px;top:1543px;background:linear-gradient(135deg,#2f5f6c,#10202a)" role="img" aria-label="Team monitoring network screens"></div>
<div class="abs thumb" style="left:512px;top:1543px;background:linear-gradient(135deg,#cfd6dd,#2b3038)" role="img" aria-label="Open computer hardware"></div>
<div class="abs thumb" style="left:845px;top:1543px;background:linear-gradient(135deg,#8fa8c2,#2a3f57)" role="img" aria-label="Engineers in a data centre"></div>

<h2 class="abs heading section-title" style="top:2338px">What Our Customers<br>Say <span class="accent">About Us</span></h2>

<div class="abs kid" role="img" aria-label="Smiling schoolboy in shirt and tie pointing upwards"></div>
<div class="abs quote-mark">&ldquo;</div>
<p class="abs quote">" Orvane Systems are reliable and supportive. Their technical knowledge is fantastic and they make sure our school network runs efficiently. Our school technician, Owen, is very approachable and friendly. He is always on hand to offer advice and support when needed."</p>
<div class="abs author">Helen Marsh, ICT Coordinator at St Aldric's Primary School</div>

<section class="abs cta">
  <div class="line">Education, Support and Installation of All Technologies</div>
  <span class="btn" style="left:846px;top:23px;width:166px;height:50px">CONTACT US</span>
</section>

<footer class="abs footer">
  <div class="brand">
    <div class="name">Orvane</div>
    <div class="tag">Education Support and Installation</div>
  </div>
  <span class="social" style="left:126px;background:#2f4c8a" aria-label="Social link"></span>
  <span class="social" style="left:179px;background:#1da1f2" aria-label="Social link"></span>
  <span class="social" style="left:232px;background:#c4302b" aria-label="Social link"></span>
  <span class="social" style="left:285px;background:#0e6bb0" aria-label="Social link"></span>

  <h4 style="left:420px"><span class="accent">SIGNUP FOR NEWSLETTER</span></h4>
  <p class="news">Would you like to recieve our exclusive blog and updates !</p>
  <div class="field">Enter Email *</div>
  <span class="btn" style="left:422px;top:217px;width:155px;height:51px">SUBSCRIBE</span>

  <h4 style="left:801px"><span class="accent">CONTACT INFO</span></h4>
  <svg class="contact-icon" style="top:100px" width="20" height="28" viewBox="0 0 20 28"><path d="M10 0a10 10 0 0 0-10 10c0 7.5 10 18 10 18s10-10.5 10-18A10 10 0 0 0 10 0z" fill="#0b6ec0"/><circle cx="10" cy="10" r="3.6" fill="#0f1a28"/></svg>
  <div class="contact-item" style="top:97px;color:#fff">Orvane Systems</div>
  <div class="contact-item" style="top:128px;font-size:14px;line-height:24px">Kestrel House, Linden Street<br>Bury Lancashire BL0 4QX</div>
  <svg class="contact-icon" style="top:200px" width="20" height="20" viewBox="0 0 24 24"><path fill="#0b6ec0" d="M6.6 10.8a15 15 0 0 0 6.6 6.6l2.2-2.2a1 1 0 0 1 1-.25 11.4 11.4 0 0 0 3.6.57 1 1 0 0 1 1 1V20a1 1 0 0 1-1 1A17 17 0 0 1 3 4a1 1 0 0 1 1-1h3.5a1 1 0 0 1 1 1 11.4 11.4 0 0 0 .57 3.6 1 1 0 0 1-.25 1z"/></svg>
  <div class="contact-item" style="top:199px">0161 555 0142</div>
  <svg class="contact-icon" style="top:245px" width="22" height="16" viewBox="0 0 22 16"><rect width="22" height="16" rx="2" fill="#0b6ec0"/><path d="M1 1l10 8 10-8" fill="none" stroke="#0f1a28" stroke-width="2"/></svg>
  <div class="contact-item" style="top:241px">info@orvane-sys.co.uk</div>

  <div class="rule"></div>
  <div class="copy">&copy;<span>ORVANE SYSTEMS LTD</span> &ndash; 2020 All rights reserved</div>
</footer>

</body>
</html>
```